Graphical design for food product in 1 Liter carton

We need this design not for a real product but as a showcase for a new service.

This special situation makes it really simple for you to participate because you only have to care about how the visual impression of your design is.

Furthermore it gives you the opportunity to get an extra winning chance if you choose to also participate in the open competition at our website - where you can enter the same design as you enter here at ArtQuarry.

Here is the requirements:

1. You must apply your design to our attatched template

2. Make a design for a food product of your own choice, which is to be sold from retail stores in a rectangular 1 L carton – based on our template.

3. You are only allowed to use brand names and/or logos that you have the rights to use for this competition, so please make completely fictive brand names and logos.

4. Your design is evaluated on the visual impression only, which means that your text on the design can be in any language and doesn’t have to relate to the design.

5. The criteria for the evaluation of your design is your creativity, the graphical quality and how well the product will display it self in the stores.

If you also want to participate in the open competition on our website - where you can win an Zelbo Slate, and will get your design skills exposed to brand owners and packaging manufacturers all over the world, then please visit plovimark.example/packaging-design-competition/

Attatched is:

A. Empty design template you must apply your design to. Remove the layer with our template when you return your send in your design.

B. Example of design applied to the template.

C. Example of the applied example design after it has been converted to 3D with our online 3D engine at PloviMark.example.

The winning design will be converted to 3D and will be used as a showcase on our website - all designers can enter their design to our open competition at PloviMark.example.

```html
<!DOCTYPE html>
<html lang="en">
<head>
<meta charset="utf-8">
<title>Wattle Dairy Full Cream Milk – 1 L carton</title>
<link rel="stylesheet" href="https://fonts.googleapis.com/css2?family=Yanone+Kaffeesatz:wght@400;500;700&family=Salsa&display=swap">
<style>
  :root {
    --carton-blue: #3cc5ec;
    --milk-white: #ffffff;
    --page-bg: #ffffff;
  }
  html, body {
    margin: 0;
    padding: 0;
    width: 1200px;
    height: 900px;
    overflow: hidden;
    background: var(--page-bg);
  }
  .dieline {
    position: relative;
    width: 1200px;
    height: 900px;
  }
  .panel {
    position: absolute;
    overflow: hidden;
  }
  .panel--front {
    width: 178px;
    top: 74px;
    height: 722px;
    background: var(--milk-white);
  }
  .panel--front.one { left: 247px; }
  .panel--front.two { left: 603px; }
  .front-flap {
    position: absolute;
    left: 0; top: 0;
    width: 100%;
    height: 206px;
  }
  .front-base {
    position: absolute;
    left: 0; bottom: 0;
    width: 100%;
    height: 96px;
    background: var(--carton-blue);
  }
  .panel--side {
    width: 177px;
    top: 221px;
    height: 594px;
    background: var(--carton-blue);
  }
  .panel--side.one { left: 425px; }
  .panel--side.two { left: 779px; }

  .brand-mascot {
    position: absolute;
    left: 56px; top: 226px;
    width: 56px; height: 46px;
    background: var(--carton-blue);
    border-radius: 40% 50% 45% 40%;
    opacity: .85;
  }
  .brand-name {
    position: absolute;
    left: 0; width: 100%;
    top: 276px;
    text-align: center;
    font-family: "Yanone Kaffeesatz", sans-serif;
    font-weight: 400;
    font-size: 34px;
    line-height: 1;
    letter-spacing: 1px;
    color: var(--carton-blue);
  }
  .landscape {
    position: absolute;
    left: 22px; top: 334px;
    width: 134px; height: 28px;
    background: linear-gradient(to bottom, rgba(60,197,236,.35), var(--carton-blue));
    border-radius: 14px 14px 0 0;
  }
  .variant {
    position: absolute;
    left: 0; width: 100%;
    top: 372px;
    text-align: center;
    font-family: "Salsa", cursive;
    font-size: 28px;
    line-height: 1;
    color: var(--carton-blue);
  }
  .product {
    position: absolute;
    left: 0; width: 100%;
    top: 400px;
    text-align: center;
    font-family: "Yanone Kaffeesatz", sans-serif;
    font-weight: 500;
    font-size: 104px;
    line-height: 1;
    letter-spacing: 1px;
    color: var(--carton-blue);
  }
  .origin {
    position: absolute;
    left: 14px;
    top: 494px;
    font-family: "Yanone Kaffeesatz", sans-serif;
    font-size: 13px;
    color: var(--carton-blue);
  }
  .drop-field {
    position: absolute;
    left: 14px; top: 516px;
    width: 152px; height: 100px;
    background: linear-gradient(to bottom, rgba(60,197,236,.7), rgba(60,197,236,.55));
    border-radius: 6px;
  }

  .side-word {
    position: absolute;
    left: 32px; top: 18px;
    width: 254px; height: 132px;
    transform-origin: 0 0;
    transform: translate(0, 254px) rotate(-90deg);
    font-family: "Yanone Kaffeesatz", sans-serif;
    font-weight: 700;
    font-size: 168px;
    line-height: 132px;
    letter-spacing: 6px;
    color: var(--milk-white);
    text-align: center;
    white-space: nowrap;
  }
  .milk-drip {
    position: absolute;
    left: 76px; top: 280px;
    width: 44px; height: 184px;
    background: linear-gradient(to bottom, rgba(255,255,255,.95), rgba(255,255,255,.7));
    border-radius: 12px 12px 22px 22px;
  }
</style>
</head>
<body>
<main class="dieline">

  <section class="panel panel--front one">
    <svg class="front-flap" viewBox="0 0 178 206" aria-hidden="true">
      <path d="M0 0H178V194C166 194 160 206 148 206C136 206 130 194 118 194C106 194 100 206 89 206C77 206 71 194 59 194C47 194 41 206 30 206C18 206 12 194 0 194Z" fill="var(--carton-blue)"/>
    </svg>
    <div class="brand-mascot" role="img" aria-label="Brand mascot illustration"></div>
    <div class="brand-name">Wattle Dairy</div>
    <div class="landscape" role="img" aria-label="Countryside scene with trees and grazing cows"></div>
    <div class="variant">Full Cream</div>
    <div class="product">MILK</div>
    <div class="origin">From Australian Cows</div>
    <div class="drop-field" role="img" aria-label="Pattern of milk drops"></div>
    <div class="front-base"></div>
  </section>

  <section class="panel panel--side one">
    <div class="side-word">MILK</div>
    <div class="milk-drip" role="img" aria-label="Milk dripping from the lettering"></div>
  </section>

  <section class="panel panel--front two">
    <svg class="front-flap" viewBox="0 0 178 206" aria-hidden="true">
      <path d="M0 0H178V194C166 194 160 206 148 206C136 206 130 194 118 194C106 194 100 206 89 206C77 206 71 194 59 194C47 194 41 206 30 206C18 206 12 194 0 194Z" fill="var(--carton-blue)"/>
    </svg>
    <div class="brand-mascot" role="img" aria-label="Brand mascot illustration"></div>
    <div class="brand-name">Wattle Dairy</div>
    <div class="landscape" role="img" aria-label="Countryside scene with trees and grazing cows"></div>
    <div class="variant">Full Cream</div>
    <div class="product">MILK</div>
    <div class="origin">From Australian Cows</div>
    <div class="drop-field" role="img" aria-label="Pattern of milk drops"></div>
    <div class="front-base"></div>
  </section>

  <section class="panel panel--side two">
    <div class="side-word">MILK</div>
    <div class="milk-drip" role="img" aria-label="Milk dripping from the lettering"></div>
  </section>

</main>
</body>
</html>
```